brownie sticker

i need a sticker to wrap around a clear rectangle box that will contain chocolate brownies. the sticker must be 17cm x 7 cm.
the sticker will be placed in the folowing direction.
7cm of the sticker on front of box, 3cm for each side of the box, and 4 cm on the bottom to seal the box closed.
I HAVE ATTACHED A VERY ROUGH PICTURE FOR YOU TO SEE POSITION AND DIRECTION OF STICKER.

Target Market(s)

our product will be mainly seen in upmarket grocery stores and farmers markets.

Requirements
Must have
• IT MUST CONTAIN THE FOLLOWING IN SMALL PRINT at the bottom of the sticker...
produced by marigolds bakehouse
48 ferncliff rd
cheltenham
vic 3192
ph: 047385916
email: marigoldsbakehouse@quillmail.test

```html
<!DOCTYPE html>
<html lang="en">
<head>
<meta charset="utf-8">
<title>Marigolds Bakehouse – Brownie Box Wrap</title>
<link rel="stylesheet" href="https://fonts.googleapis.com/css2?family=Marcellus&family=Open+Sans:wght@400&display=swap">
<style>
  :root {
    --cocoa: #8f5226;
    --cocoa-light: #a8652f;
    --cocoa-dark: #5e3014;
    --gold-light: #fbe08e;
    --gold-mid: #d9a441;
    --gold-deep: #9c6a1c;
    --cream: #fbf2c6;
    --cream-edge: #f1dc98;
    --ink: #552913;
    --print: #3a1b09;
  }
  * { margin: 0; padding: 0; box-sizing: border-box; }
  html, body {
    width: 1200px;
    height: 2912px;
    overflow: hidden;
    background: var(--cocoa);
  }
  .wrap-label {
    position: relative;
    width: 1200px;
    height: 2912px;
    overflow: hidden;
  }
  .flourish-field {
    position: absolute;
    inset: 0;
    background:
      radial-gradient(ellipse at 50% 50%, var(--cocoa-light) 0%, var(--cocoa) 55%, var(--cocoa-dark) 100%);
  }
  .seal-medallion {
    position: absolute;
    left: 0;
    top: 860px;
    width: 1200px;
    height: 1200px;
  }
  .brand-name {
    position: absolute;
    left: 0;
    width: 1200px;
    top: 1395px;
    text-align: center;
    font-family: "Marcellus", serif;
    font-weight: 400;
    color: var(--ink);
  }
  .brand-name .brand-main {
    display: block;
    font-size: 80px;
    letter-spacing: 4px;
    line-height: 1;
  }
  .brand-name .brand-sub {
    display: block;
    margin-top: 24px;
    font-size: 36px;
    letter-spacing: 16px;
    line-height: 1;
  }
  .base-dome {
    position: absolute;
    left: 0;
    top: 2520px;
    width: 1200px;
    height: 392px;
  }
  .maker-details {
    position: absolute;
    left: 16px;
    top: 2748px;
    font-family: "Open Sans", sans-serif;
    font-size: 29px;
    line-height: 40px;
    color: var(--print);
    text-transform: uppercase;
    white-space: nowrap;
  }
</style>
</head>
<body>
<main class="wrap-label">
  <div class="flourish-field" role="img" aria-label="Dark chocolate swirling flourish pattern over a warm cocoa background"></div>

  <svg class="seal-medallion" viewBox="0 0 1200 1200" aria-hidden="true">
    <defs>
      <linearGradient id="ringGold" x1="0" y1="0" x2="1" y2="1">
        <stop offset="0" stop-color="var(--gold-light)"/>
        <stop offset="0.45" stop-color="var(--gold-mid)"/>
        <stop offset="0.75" stop-color="var(--gold-deep)"/>
        <stop offset="1" stop-color="var(--gold-light)"/>
      </linearGradient>
      <linearGradient id="ringGoldInner" x1="1" y1="1" x2="0" y2="0">
        <stop offset="0" stop-color="var(--gold-light)"/>
        <stop offset="0.5" stop-color="var(--gold-mid)"/>
        <stop offset="1" stop-color="var(--gold-deep)"/>
      </linearGradient>
      <radialGradient id="creamFace" cx="0.5" cy="0.5" r="0.5">
        <stop offset="0.7" stop-color="var(--cream)"/>
        <stop offset="1" stop-color="var(--cream-edge)"/>
      </radialGradient>
    </defs>
    <circle class="ring-outer" cx="600" cy="600" r="596" fill="url(#ringGold)"/>
    <circle class="ring-inner" cx="600" cy="600" r="520" fill="url(#ringGoldInner)"/>
    <circle class="ring-shadow" cx="600" cy="600" r="482" fill="var(--cocoa-dark)"/>
    <circle class="medallion-face" cx="612" cy="612" r="468" fill="url(#creamFace)"/>
  </svg>

  <h1 class="brand-name">
    <span class="brand-main">MARIGOLDS</span>
    <span class="brand-sub">BAKEHOUSE</span>
  </h1>

  <svg class="base-dome" viewBox="0 0 1200 392" aria-hidden="true">
    <defs>
      <linearGradient id="domeGold" x1="0" y1="0" x2="0" y2="1">
        <stop offset="0" stop-color="var(--gold-mid)"/>
        <stop offset="0.25" stop-color="var(--gold-light)"/>
        <stop offset="1" stop-color="var(--gold-mid)"/>
      </linearGradient>
    </defs>
    <path d="M0 392 L0 150 Q600 -60 1200 150 L1200 392 Z" fill="var(--gold-deep)"/>
    <path d="M0 392 L0 170 Q600 -30 1200 170 L1200 392 Z" fill="url(#domeGold)"/>
  </svg>

  <p class="maker-details">
    Produced by Marigolds Bakehouse<br>
    48 Ferncliff Rd, Hollowmere, VIC 3911<br>
    Tel: 047385916<br>
    Email: marigoldsbakehouse@quillmail.test
  </p>
</main>
</body>
</html>
```